KA VERLINE

We need a letterhead design for an Image & Etiquette Consultancy company based in Singapore.

The services we provide are Personal Image Consultation, Image & Etiquette Workshop for schools and corporate.

The design should have our corporate colour as seen in the logo files I have uploaded.

Since our company helps clients with their image, the design should be aesthetically very appealing. It should reflect a very classy & elegant feel.

I will print the letterhead using my printer but most of the time will use it to write letters to my clients therefore the format should include MS Word.

```html
<!DOCTYPE html>
<html lang="en">
<head>
<meta charset="utf-8">
<title>Ka Verline Letterhead</title>
<link rel="stylesheet" href="https://fonts.googleapis.com/css2?family=Jura:wght@400;500&family=Open+Sans:wght@400&display=swap">
<style>
  :root {
    --backdrop: #e2e3e2;
    --paper: #ffffff;
    --plum: #2e1a3f;
    --gold: #c9a227;
    --ink: #3a3a3a;
  }
  * { margin: 0; padding: 0; box-sizing: border-box; }
  html, body {
    width: 1200px;
    height: 1200px;
    overflow: hidden;
    background: var(--backdrop);
  }
  .letterhead {
    position: absolute;
    left: 273px;
    top: 138px;
    width: 653px;
    height: 923px;
    background: var(--paper);
    overflow: hidden;
  }
  .brand-name {
    position: absolute;
    left: 42px;
    top: 44px;
    font-family: "Jura", sans-serif;
    font-weight: 400;
    font-size: 36px;
    letter-spacing: 1px;
    color: var(--plum);
    line-height: 1;
  }
  .footer {
    position: absolute;
    left: 44px;
    top: 822px;
    font-family: "Open Sans", sans-serif;
    color: var(--ink);
  }
  .footer-company {
    font-family: "Jura", sans-serif;
    font-weight: 500;
    font-size: 16px;
    letter-spacing: 0.6px;
    color: var(--plum);
    margin-bottom: 3px;
  }
  .footer-line {
    font-size: 9.5px;
    line-height: 14.5px;
  }
  .corner-accent {
    position: absolute;
    right: 0;
    bottom: 0;
    width: 275px;
    height: 101px;
    background: linear-gradient(160deg, rgba(255,255,255,0) 35%, rgba(201,162,39,0.55) 62%, var(--plum) 80%);
  }
</style>
</head>
<body>
  <main class="letterhead">
    <div class="brand-name">KA VERLINE</div>

    <footer class="footer">
      <div class="footer-company">Ka Verline Limited</div>
      <div class="footer-line">Your Long address with ode no. &nbsp;| &nbsp;your licence no.: xxx xxx xxx xx</div>
      <div class="footer-line">Phone: 000 000 000 | Email: yourname@kaverline.com</div>
      <div class="footer-line">Website: www.kaverline.com</div>
    </footer>

    <div class="corner-accent" role="img" aria-label="Decorative gold and plum corner flourish"></div>
  </main>
</body>
</html>
```